Veltrano - Mechanic/Collision Center Business Card

We're looking for a business card design for our mechanic/ collision repair shop.

Can be with colours or monochromatic.

See the attached files.

Many thanks

```html
<!DOCTYPE html>
<html lang="pt">
<head>
<meta charset="utf-8">
<title>Veltrano – Business Card</title>
<link href="https://fonts.googleapis.com/css2?family=Montserrat:wght@400;600;700;800&display=swap" rel="stylesheet">
<style>
  :root {
    --page: #ededed;
    --slate: #465b67;
    --card: #ffffff;
    --ink: #222528;
    --ink-soft: #3a3d40;
    --muted: #5f6b72;
    --white: #ffffff;
  }
  * { box-sizing: border-box; margin: 0; padding: 0; }
  html, body {
    width: 1200px; height: 811px; overflow: hidden;
    background: var(--page);
    font-family: "Montserrat", Arial, sans-serif;
  }
  .canvas { position: relative; width: 1200px; height: 811px; }
  .card {
    position: absolute; left: 296px; width: 608px; height: 368px;
    background: var(--card);
    box-shadow: 3px 4px 6px rgba(0,0,0,0.28);
    overflow: hidden;
  }
  .card--front { top: 25px; }
  .card--back { top: 420px; height: 363px; }

  /* front */
  .front-band {
    position: absolute; left: 0; top: 0; width: 100%; height: 291px;
    background: var(--slate);
    border-bottom: 1px solid #1f2a30;
  }
  .front-brand {
    position: absolute; left: 0; width: 100%; top: 140px;
    display: flex; justify-content: center; align-items: center; gap: 14px;
    color: var(--white);
  }
  .brand-mark { width: 22px; height: 22px; background: currentColor; }
  .brand-name {
    font-weight: 800; font-size: 54px; letter-spacing: 1px; line-height: 1;
  }
  .front-email {
    position: absolute; left: 0; width: 100%; top: 312px;
    text-align: center; font-size: 10px; letter-spacing: 3px;
    color: var(--muted);
  }

  /* back */
  .back-tab {
    position: absolute; left: 323px; top: 0; width: 227px; height: 32px;
    background: var(--slate);
  }
  .person { position: absolute; left: 58px; top: 60px; }
  .person-name { font-weight: 700; font-size: 27px; color: var(--ink); line-height: 1.1; }
  .person-role { font-size: 13.5px; color: var(--muted); margin-top: 2px; }
  .accent-dash {
    position: absolute; left: 58px; top: 158px; width: 37px; height: 4px;
    background: var(--slate);
  }
  .back-brand {
    position: absolute; left: 323px; width: 227px; top: 94px;
    display: flex; justify-content: center; align-items: center; gap: 10px;
    color: var(--ink);
  }
  .back-brand .brand-name { font-size: 30px; }
  .back-brand .brand-mark { width: 14px; height: 14px; }

  .address { position: absolute; left: 58px; top: 242px; }
  .contact { position: absolute; left: 326px; top: 242px; }
  .company { font-weight: 700; font-size: 13.5px; color: var(--slate); }
  .line { font-size: 13.5px; color: var(--ink-soft); line-height: 22.5px; }
  .address .company, .contact .line:first-child { margin-bottom: 7px; line-height: 18px; }
</style>
</head>
<body>
<main class="canvas">
  <section class="card card--front">
    <div class="front-band"></div>
    <div class="front-brand">
      <span class="brand-mark" aria-hidden="true"></span>
      <span class="brand-name">VELTRANO</span>
    </div>
    <p class="front-email">veltrano.oficina@mail.pt</p>
  </section>

  <section class="card card--back">
    <div class="back-tab"></div>
    <div class="person">
      <h1 class="person-name">Tomás Valbrena</h1>
      <p class="person-role">Manager/+351 912 480 317</p>
    </div>
    <div class="accent-dash"></div>
    <div class="back-brand">
      <span class="brand-mark" aria-hidden="true"></span>
      <span class="brand-name">VELTRANO</span>
    </div>
    <div class="address">
      <p class="company">Veltrano, LDA</p>
      <p class="line">Rua das Oficinas, 42</p>
      <p class="line">1900-210 Lisboa</p>
    </div>
    <div class="contact">
      <p class="line">+351 213 574 906 (Mobile)</p>
      <p class="line">veltrano.oficina@mail.pt</p>
      <p class="line">www.veltrano.pt/oficina</p>
    </div>
  </section>
</main>
</body>
</html>
```